After-School Program - End of the Year Mailing to Donors

We would like to highlight some of our accomplishments from the year and ask people to donate to our organization. We are a non-profit organization that serves underprivileged children with after school programs. We want a 6x9 flyer with printing on both sides that we can mail out soon. The flyer should be a mix of great photos, some text, and a space for mailing and return address.

Target Market(s)

regular donors

Industry/Entity Type

Education

Font styles to use
Serif

Colors

Designer to choose colors to be used in the design.

Requirements
Must have
• Photos, text, a space on one side for a mailing label, a return address, and a stamp.
Nice to have
• attractive, eye-catching
Should not have
• boring

```html
<!DOCTYPE html>
<html lang="en">
<head>
<meta charset="utf-8">
<title>Riverside Youth Learning House – Donor Mailer</title>
<link href="https://fonts.googleapis.com/css2?family=Arimo:wght@400;700&display=swap" rel="stylesheet">
<style>
  :root {
    --paper: #ffffff;
    --sun: #fbeb21;
    --ink: #111111;
    --rule: #8a8a8a;
    --stamp: #eeeeee;
  }
  html, body {
    margin: 0;
    padding: 0;
    overflow: hidden;
    background: var(--paper);
  }
  .mailer {
    position: relative;
    width: 1200px;
    height: 801px;
    overflow: hidden;
    background: var(--paper);
    font-family: "Arimo", Arial, sans-serif;
    color: var(--ink);
  }
  .sun-splash {
    position: absolute;
    inset: 0;
    width: 1200px;
    height: 801px;
  }
  .copy {
    position: absolute;
    margin: 0;
    font-size: 21px;
    line-height: 26.6px;
    text-align: justify;
  }
  .copy p { margin: 0; }
  .copy strong { font-weight: 700; }
  .copy--appeal { left: 51px; top: 49px; width: 408px; }
  .copy--programs { left: 49px; top: 238px; width: 408px; }
  .copy--ask { left: 53px; top: 556px; width: 505px; }
  .copy--give { left: 53px; top: 663px; width: 505px; text-align: left; }
  .brand {
    position: absolute;
    left: 536px;
    top: 150px;
    width: 200px;
    display: flex;
    align-items: center;
    gap: 10px;
  }
  .brand__dot {
    flex: 0 0 auto;
    width: 34px;
    height: 34px;
    border-radius: 50%;
    background: var(--sun);
  }
  .brand__name {
    font-size: 18px;
    font-weight: 700;
    line-height: 22px;
  }
  .stamp-box {
    position: absolute;
    left: 1000px;
    top: 51px;
    width: 131px;
    height: 174px;
    box-sizing: border-box;
    border: 8px dotted var(--stamp);
  }
  .stamp-box::after {
    content: "";
    position: absolute;
    left: 14px;
    top: 16px;
    right: 14px;
    bottom: 16px;
    border: 7px solid var(--stamp);
  }
  .address-line {
    position: absolute;
    left: 700px;
    width: 419px;
    height: 0;
    border-top: 1px solid var(--rule);
  }
</style>
</head>
<body>
<main class="mailer">
  <svg class="sun-splash" viewBox="0 0 1200 801" aria-hidden="true">
    <path fill="var(--sun)" d="M0 0 L370 0 L362 14 L380 8 L400 22 L420 16 L440 30 L462 24 L485 34 L505 28 L520 40 L510 60 L500 92 L508 110 L490 140 L498 162 L470 190 L478 210 L446 232 L452 250 L420 262 L400 284 L372 300 L382 318 L350 336 L336 356 L320 380 L300 396 L340 412 L360 420 L395 424 L420 440 L460 460 L500 480 L540 500 L560 530 L590 560 L600 590 L622 620 L640 650 L652 680 L668 710 L672 740 L684 770 L690 801 L0 801 Z"/>
  </svg>

  <div class="copy copy--appeal">
    <p><strong>Riverside Youth Learning House</strong> is in the middle of its 24th year of ministry and we need your help to finish our year strong!&nbsp; We need another <strong>$35,000</strong> from our individual donors to help us meet our budget.</p>
  </div>

  <div class="copy copy--programs">
    <p>We serve over <strong>150 children</strong> each day at our four sites with a unique mix of homework help, a focus on <strong>literacy, enrichment classes</strong> - including music lessons, and a caring environment based on <strong>God’s love.</strong></p>
  </div>

  <div class="copy copy--ask">
    <p><strong>Please help us</strong> continue to impact children and families through our high quality faith-based educational programs.</p>
  </div>

  <div class="copy copy--give">
    <p>To contribute, please visit<br><strong>www.brightpath-kids.org</strong><br>and click on the DONATE button.</p>
  </div>

  <div class="brand">
    <span class="brand__dot"></span>
    <span class="brand__name">Riverside Youth Learning House</span>
  </div>

  <div class="stamp-box" aria-label="Stamp area"></div>

  <div class="address-line" style="top:501px"></div>
  <div class="address-line" style="top:574px"></div>
  <div class="address-line" style="top:649px"></div>
  <div class="address-line" style="top:723px"></div>
</main>
</body>
</html>
```